Marketing flyer to advertise course vacancies

I am seeking something that is eye catching
A document that I can edit to list our courses and prices to try and gain further bookings on the courses.
I have attached our company logo, our website is www.brightwaveskills.com.au for your viewing.
Our motto is Train today for a safer tomorrow, we would want this on the brochure.

```html
<!DOCTYPE html>
<html lang="en">
<head>
<meta charset="utf-8">
<title>Brightwave Skills – Courses and Prices</title>
<link rel="stylesheet" href="https://fonts.googleapis.com/css2?family=Anton&family=Poppins:wght@400;500;600;700&display=swap">
<style>
  :root {
    --stage: #a7a7a7;
    --paper: #ffffff;
    --haze: #e4e5e7;
    --red: #d92632;
    --ink: #1d1d1f;
    --line: #3a3a3a;
    --photo-a: #c9a15a;
    --photo-b: #5d6b78;
  }
  * { margin: 0; padding: 0; box-sizing: border-box; }
  html, body { width: 1200px; height: 879px; overflow: hidden; background: var(--stage); }
  body { font-family: "Poppins", sans-serif; color: var(--ink); }

  .flyer {
    position: absolute; left: 79px; top: 71px; width: 1035px; height: 732px;
    background: linear-gradient(125deg, var(--paper) 0%, var(--paper) 30%, var(--haze) 55%, var(--paper) 72%, var(--haze) 100%);
    overflow: hidden;
  }
  .flyer-shapes { position: absolute; inset: 0; }

  .brand {
    position: absolute; left: 20px; top: 58px; width: 190px;
    display: flex; align-items: center; justify-content: center; gap: 8px;
    font-weight: 700; font-size: 18px; color: var(--red);
  }
  .brand-dot { width: 16px; height: 16px; border-radius: 50%; background: var(--red); }

  .section-tab {
    position: absolute; left: 34px; top: 141px; height: 23px; width: 266px;
    background: var(--red); color: var(--paper);
    clip-path: polygon(0 0, 92% 0, 100% 100%, 0 100%);
    font-weight: 600; font-size: 14.5px; line-height: 23px; padding-left: 5px;
  }

  .headline {
    position: absolute; left: 300px; top: 25px; width: 440px;
    font-family: "Anton", sans-serif; color: var(--paper);
    font-size: 49px; line-height: 57px; letter-spacing: 2.5px; text-align: center;
  }
  .headline span { display: block; }
  .headline span + span { margin-left: 42px; }

  .price-table {
    position: absolute; border-collapse: collapse; background: var(--paper);
    font-size: 12.6px; table-layout: fixed;
  }
  .price-table th, .price-table td {
    border: 0.8px solid var(--line); height: 22.2px; padding: 0 4px; white-space: nowrap;
  }
  .price-table th { color: var(--red); font-weight: 600; text-align: center; }
  .price-table th:first-child { text-align: left; }
  .price-table td + td { text-align: center; }
  .price-table.left { left: 34px; top: 182px; width: 501px; }
  .price-table.right { left: 530px; top: 182px; width: 477px; }
  .price-table.right td:first-child, .price-table.right th:first-child { padding-left: 6px; }

  .contact {
    position: absolute; left: 34px; top: 665px;
    color: var(--paper); font-size: 11.8px; line-height: 14.6px;
  }
  .site {
    position: absolute; left: 570px; top: 689px; width: 465px; text-align: center;
    color: var(--paper); font-size: 24px; line-height: 40px;
  }
</style>
</head>
<body>
  <main class="flyer">
    <svg class="flyer-shapes" width="1035" height="732" viewBox="0 0 1035 732">
      <defs>
        <linearGradient id="photoTone" x1="0" y1="0" x2="1" y2="1">
          <stop offset="0" stop-color="var(--photo-a)"/>
          <stop offset="1" stop-color="var(--photo-b)"/>
        </linearGradient>
      </defs>
      <polygon points="150,0 210,0 341,161 285,161" fill="#ececed"/>
      <polygon points="210,0 772,0 865,161 341,161" fill="var(--red)"/>
      <polygon role="img" aria-label="Photo of a smiling warehouse worker in a hard hat and high-visibility vest beside a forklift" points="740,0 1035,0 1035,161 865,161" fill="url(#photoTone)"/>
      <polygon points="0,649 384,649 476,732 0,732" fill="var(--ink)"/>
      <polygon points="430,691 475,691 518,732 476,732" fill="var(--red)"/>
      <polygon points="520,691 1035,691 1035,732 564,732" fill="var(--red)"/>
    </svg>

    <div class="brand"><span class="brand-dot"></span>Brightwave Skills</div>

    <h1 class="headline"><span>TRAIN TODAY FOR A</span><span>SAFER TOMORROW</span></h1>

    <div class="section-tab">LIST OUR COURSES AND PRICES</div>

    <table class="price-table left">
      <colgroup><col style="width:277px"><col style="width:93px"><col style="width:131px"></colgroup>
      <thead><tr><th>COURSES</th><th>DURATION</th><th>COST</th></tr></thead>
      <tbody>
        <tr><td>Safe Work at Heights</td><td>7 Day</td><td>$225</td></tr>
        <tr><td>Confined Space</td><td>7 Day</td><td>$225</td></tr>
        <tr><td>Swift Water Rescue</td><td>7 Day</td><td>$225</td></tr>
        <tr><td>Fire Extinguisher Training</td><td>7 Day</td><td>$225</td></tr>
        <tr><td>Fire Warden Training</td><td>7 Day</td><td>$225</td></tr>
        <tr><td>Breathing Apparatus Training</td><td>7 Day</td><td>$225</td></tr>
        <tr><td>Emergency Response Team Training</td><td>7 Day</td><td>$225</td></tr>
        <tr><td>Provide Emergency Care</td><td>7 Day</td><td>$225</td></tr>
        <tr><td>Road Accident Rescue</td><td>7 Day</td><td>$225</td></tr>
        <tr><td>Gas Test Atmospheres</td><td>7 Day</td><td>$225</td></tr>
        <tr><td>Confined Space Rescue</td><td>7 Day</td><td>$225</td></tr>
        <tr><td>Vertical Rescue</td><td>7 Day</td><td>$225</td></tr>
        <tr><td>Operate Breathing Apparatus</td><td>7 Day</td><td>$225</td></tr>
        <tr><td>BG4</td><td>7 Day</td><td>$225</td></tr>
        <tr><td>Render Hazardous Materials Incidents Safe</td><td>7 Day</td><td>$225</td></tr>
        <tr><td>Respond to Wildfire</td><td>7 Day</td><td>$225</td></tr>
        <tr><td>Senior First Aid Training</td><td>7 Day</td><td>$225</td></tr>
        <tr><td>Low Voltage Switchboard Rescue</td><td>7 Day</td><td>$225</td></tr>
        <tr><td>Issue Work Permits</td><td>7 Day</td><td>$225</td></tr>
      </tbody>
    </table>

    <table class="price-table right">
      <colgroup><col style="width:289px"><col style="width:94px"><col style="width:94px"></colgroup>
      <thead><tr><th>COURSES</th><th>DURATION</th><th>COST</th></tr></thead>
      <tbody>
        <tr><td>Fatigue Management Training (Supervisors)</td><td>7 Day</td><td>$225</td></tr>
        <tr><td>Fatigue Management Training (Workers)</td><td>7 Day</td><td>$225</td></tr>
        <tr><td>Overhead Gantry Crane Ticket</td><td>7 Day</td><td>$225</td></tr>
        <tr><td>Telehandler Ticket</td><td>7 Day</td><td>$225</td></tr>
        <tr><td>Loader Ticket</td><td>7 Day</td><td>$225</td></tr>
        <tr><td>Skidsteer Ticket</td><td>7 Day</td><td>$225</td></tr>
        <tr><td>Excavator Ticket</td><td>7 Day</td><td>$225</td></tr>
        <tr><td>High Risk Work Licence Tickets</td><td>7 Day</td><td>$225</td></tr>
        <tr><td>Standard 11</td><td>7 Day</td><td>$225</td></tr>
        <tr><td>Perform Tower Rescue</td><td>7 Day</td><td>$225</td></tr>
        <tr><td>Forklift (LF) Ticket</td><td>7 Day</td><td>$225</td></tr>
        <tr><td>EWP (WP) Ticket</td><td>7 Day</td><td>$225</td></tr>
        <tr><td>Dogging (DG) Ticket</td><td>7 Day</td><td>$225</td></tr>
        <tr><td>Non slew crane (CN) Ticket</td><td>7 Day</td><td>$225</td></tr>
        <tr><td>Vehicle Loading Crane (CV) Ticket</td><td>7 Day</td><td>$225</td></tr>
        <tr><td>Basic Scaffolding (SB) Ticket</td><td>7 Day</td><td>$225</td></tr>
        <tr><td>Intermediate scaffolding (SI) Ticket</td><td>7 Day</td><td>$225</td></tr>
        <tr><td>Advanced scaffolding (SA) Ticket</td><td>7 Day</td><td>$225</td></tr>
        <tr><td>Basic Rigging (RB) Ticket</td><td>7 Day</td><td>$225</td></tr>
        <tr><td>Health and Safety Representative Training</td><td>7 Day</td><td>$225</td></tr>
        <tr><td>Risk Management</td><td>7 Day</td><td>$225</td></tr>
      </tbody>
    </table>

    <p class="contact">FOR A COMPLETE LIST OF WHAT WE CAN OFFER YOU<br>PLEASE DO NOT HESITATE IN CONTACTING OUR OFFICE ON<br>ph : 07 4000 1234 or email- ADMIN@BRIGHTWAVESKILLS.COM.AU</p>

    <p class="site">www.brightwaveskills.com.au</p>
  </main>
</body>
</html>
```